Web Site for Strategy and Technology Consulting Company

We are looking for a website design that engages potential customers to understand our services and contact us. In this contest, we are looking for a homepage design, but the winning designer will be favored for the design of some of the more complicated interior pages of the site. An additional contest (or contests) for these pages will be added soon.

PLATROM AND RESPONSIVE DESIGN
The site will be implemented in WordPress using the Elementor page builder.
We are looking for a design that will look good on phones are well as laptop browsers.

UPLOADED FILES INCLUDE:
1a A wireframe of the homepage we are looking for. The Uploaded PDF also includes a draft of the text proposed for the homepage. Designers are free to go beyond the wireframe, but all elements of the wireframe should be included.
1b A Word document with the draft text of the homepage.
2a-d The Norvalith logo. Two versions are included – a dark version which works well against a light background, and a light version which works well against a dark background.
3 The Norvalith color palette with HEX and RGB values. Designers are not limited to this palette, but colors should be complementary.
4 A draft of the homepage menu
5 Service sheets with information on the services we provide

MORE ABOUT NORVALITH
Norvalith is a consulting company focused on transforming businesses through software. Our tagline, “Transformation Delivered,” recognizes the gap business often have between business transformation and the software they end up with. By listening to our customers and understanding their vision and where they are, we help get our customers where they want to go.

We increase our capability by working with many consultants and partners, allowing us to provide our customers with the best people and the software that best suits them.

Industry/Entity Type

Consulting

Number of Pages Required

1 page

Font styles to use
Sans Serif

Requirements
Must have
• the content represented on the wireframe uploaded
Nice to have
• interactive features, such as roll-over icons that reveal additional information

```html
<!DOCTYPE html>
<html lang="en">
<head>
<meta charset="utf-8">
<title>Norvalith — Transformation Delivered</title>
<link rel="stylesheet" href="https://fonts.googleapis.com/css2?family=Poppins:wght@300;400;500;600&display=swap">
<style>
:root{
  --ink:#2e2e2e;
  --text:#444;
  --muted:#6b6b6b;
  --grey:#7b7b7b;
  --band:#f3f3f3;
  --line:#d9d9d9;
  --dark:#262626;
  --bar:#4a4a4a;
  --star:#f7941d;
  --white:#fff;
}
*{box-sizing:border-box;margin:0;padding:0}
html,body{width:1200px;height:4785px;overflow:hidden}
body{font-family:'Poppins',sans-serif;color:var(--text);background:var(--white);position:relative}
.abs{position:absolute}
.ph{position:absolute;border-radius:10px}

/* header */
.brand{left:80px;top:30px;font-size:56px;font-weight:400;color:var(--ink);letter-spacing:-1px;line-height:1}
.nav{right:85px;top:48px;display:flex;align-items:center;gap:38px;font-size:15px;color:var(--ink)}
.nav .cta{background:var(--grey);color:var(--white);padding:13px 26px;font-size:14px}

/* hero */
.hero{left:0;top:133px;width:1200px;height:657px;clip-path:polygon(0 0,100% 0,100% 612px,0 100%);
  background:linear-gradient(90deg,#f1f2f2 0%,#eceeee 38%,#9aa0a3 60%,#3b4148 80%,#6b6258 100%)}
.hero-kicker{left:129px;top:236px;font-size:25px;color:var(--muted)}
.hero-title{left:126px;top:292px;font-size:40px;line-height:51px;font-weight:400;color:var(--ink)}
.hero-sub{left:126px;top:394px;font-size:20px;color:var(--ink)}
.btn{background:var(--grey);color:var(--white);display:flex;align-items:center;justify-content:center;font-size:16px;letter-spacing:.3px}
.hero-btn{left:129px;top:462px;width:187px;height:66px}

/* section headings */
.h2{font-size:60px;font-weight:500;color:var(--grey);line-height:1}
.body{font-size:15px;line-height:31px;color:var(--text)}
.checks{list-style:none}
.checks li{position:relative;padding-left:62px;font-size:15px;line-height:26px;margin-bottom:14px}
.checks svg{position:absolute;left:30px;top:4px}

/* how we work */
.band-how{left:0;top:1440px;width:1200px;height:1060px;background:var(--band);clip-path:polygon(0 85px,100% 0,100% 100%,0 100%)}
.card{position:absolute;background:var(--band);border:1.5px solid var(--line);border-radius:6px;display:flex;align-items:center}
.card.active{background:var(--white);border:2px solid #9a9a9a}
.card .ic{width:96px;height:96px;border-radius:50%;border:3px dashed #9a9a9a;margin-left:18px;flex:none;display:flex;align-items:center;justify-content:center}
.card .ic span{width:74px;height:74px;border-radius:50%;background:var(--grey);display:flex;align-items:center;justify-content:center;color:var(--white);font-size:15px;font-style:normal;text-align:center;line-height:1}
.card h3{font-size:24px;font-weight:400;color:var(--ink);margin-bottom:8px}
.card p{font-size:15px;line-height:24px;color:var(--muted)}
.card .txt{margin-left:34px}

/* testimonials */
.band-test{left:0;top:3140px;width:1200px;height:730px;background:var(--band);clip-path:polygon(0 55px,100% 0,100% 680px,0 100%)}
.quote{position:absolute;width:502px;height:333px;background:var(--grey);border-radius:40px;color:var(--white)}
.quote .name{position:absolute;left:132px;top:26px;font-size:19px}
.quote .stars{position:absolute;left:132px;top:58px;color:var(--star);font-size:20px;letter-spacing:2px}
.quote .mark{position:absolute;right:48px;top:18px;font-size:90px;line-height:1;font-weight:600}
.quote p{position:absolute;left:38px;right:40px;top:120px;font-size:15px;line-height:26px}
.avatar{position:absolute;width:112px;height:112px;border-radius:50%;border:5px solid var(--white);background:linear-gradient(160deg,#e9e9e9,#b9b9b9)}
.arrow{position:absolute;width:34px;height:34px;border-radius:50%;background:var(--grey);color:var(--white);display:flex;align-items:center;justify-content:center;font-size:18px}

/* technologies */
.tech{position:absolute;top:4118px;height:80px;display:flex;align-items:center;justify-content:center;font-size:36px;font-weight:500;color:var(--bar)}

/* footer */
.footer{left:0;top:4290px;width:1200px;height:495px;background:var(--dark);clip-path:polygon(0 80px,100% 0,100% 100%,0 100%)}
.f-brand{left:76px;top:4510px;font-size:52px;color:var(--white);letter-spacing:-1px}
.socials{left:122px;top:4592px;display:flex;gap:6px}
.socials span{width:34px;height:34px;border:1.5px solid #888;display:block}
.f-head{font-size:20px;color:var(--white);font-weight:500}
.f-head::after{content:"";display:block;width:44px;height:3px;background:var(--white);margin-top:8px}
.f-links{list-style:none;font-size:15px;color:#ddd}
.f-links li{margin-bottom:12px;display:flex;align-items:center;gap:18px}
.f-links li::before{content:"";width:9px;height:9px;background:#aaa}
.f-contact{font-size:17px;color:var(--white)}
.f-contact .row{display:flex;align-items:center;gap:20px;margin-bottom:22px}
.f-contact .box{width:32px;height:32px;border:1.5px solid #888;display:flex;align-items:center;justify-content:center;flex:none}
.copy{left:0;top:4723px;width:1200px;height:62px;background:var(--bar);color:#ddd;font-size:14px;display:flex;align-items:center;justify-content:center}
</style>
</head>
<body>

<!-- header -->
<div class="abs brand">Norvalith</div>
<nav class="abs nav"><span>About Us</span><span>Services</span><span>Insights</span><span>Join Us</span><span class="cta">Contact Us</span></nav>

<!-- hero -->
<div class="abs hero" role="img" aria-label="Photo of a consultant in a suit working on a laptop in a bright office"></div>
<div class="abs hero-kicker">Norvalith</div>
<h1 class="abs hero-title">Transformation Delivered<br>Consulting company</h1>
<div class="abs hero-sub">focused on transforming businesses through software</div>
<div class="abs btn hero-btn">READ MORE</div>

<!-- our story -->
<h2 class="abs h2" style="left:82px;top:858px">Our Story</h2>
<p class="abs body" style="left:86px;top:944px;width:509px;text-align:justify">We do more for our customers than implement software. We listen. We work to understand where they are in their transformation journey and where they want to go. We partner with them to clear the roadblocks that stand in their way, ensuring they reach their destination. At Norvalith, we:</p>
<ul class="abs checks" style="left:86px;top:1124px;width:520px">
  <li><svg width="20" height="18" viewBox="0 0 20 18"><rect x="1" y="3" width="14" height="14" fill="none" stroke="#555" stroke-width="1.6"/><path d="M4 9l4 4 10-11" fill="none" stroke="#555" stroke-width="2"/></svg>Focus on business value, with an emphasis on delivering value quickly.</li>
  <li><svg width="20" height="18" viewBox="0 0 20 18"><rect x="1" y="3" width="14" height="14" fill="none" stroke="#555" stroke-width="1.6"/><path d="M4 9l4 4 10-11" fill="none" stroke="#555" stroke-width="2"/></svg>Meet our customers where they are without backing them up to the beginning of their journey.</li>
  <li><svg width="20" height="18" viewBox="0 0 20 18"><rect x="1" y="3" width="14" height="14" fill="none" stroke="#555" stroke-width="1.6"/><path d="M4 9l4 4 10-11" fill="none" stroke="#555" stroke-width="2"/></svg>Provide a wide range of services, from strategy to product support.</li>
  <li><svg width="20" height="18" viewBox="0 0 20 18"><rect x="1" y="3" width="14" height="14" fill="none" stroke="#555" stroke-width="1.6"/><path d="M4 9l4 4 10-11" fill="none" stroke="#555" stroke-width="2"/></svg>Commit to our customer’s long-term success.</li>
</ul>
<p class="abs body" style="left:83px;top:1366px">Norvalith is business transformation, delivered.</p>
<div class="ph" style="left:657px;top:946px;width:394px;height:292px;background:linear-gradient(135deg,#cfc6bb,#6e6a66 60%,#3d3a38)" role="img" aria-label="Photo of a team gathered around a laptop"></div>
<div class="ph" style="left:845px;top:1128px;width:269px;height:224px;background:linear-gradient(135deg,#8a7d90,#3f4450 55%,#a08060);border:4px solid #fff" role="img" aria-label="Photo of colleagues working together at a desk"></div>

<!-- how we work -->
<div class="abs band-how"></div>
<h2 class="abs h2" style="left:0;width:1200px;text-align:center;top:1578px">How We Work</h2>
<p class="abs body" style="left:165px;width:870px;top:1662px;text-align:center">During our early years, Norvalith focused only on business transformation. We came to realize that successful transformation often depended on quality software implementations, and often more than one. Now we focus on five things, the five things most businesses need to reach their goals.</p>

<div class="card active" style="left:129px;top:1823px;width:455px;height:134px"><div class="ic"><span>
<svg width="30" height="34" viewBox="0 0 30 34"><rect x="3" y="2" width="24" height="30" rx="3" fill="none" stroke="#fff" stroke-width="2"/><circle cx="15" cy="17" r="5" fill="none" stroke="#fff" stroke-width="2"/></svg></span></div>
<div class="txt"><h3>Business Transformation</h3><p>Define and execute your<br>strategy.</p></div></div>

<div class="card" style="left:616px;top:1823px;width:454px;height:134px"><div class="ic"><span>
<svg width="34" height="30" viewBox="0 0 34 30"><circle cx="9" cy="8" r="5" fill="#fff"/><rect x="3" y="15" width="12" height="12" fill="#fff"/><rect x="17" y="6" width="15" height="11" fill="none" stroke="#fff" stroke-width="2"/></svg></span></div>
<div class="txt"><h3>ERP Implementations</h3><p>Assess, upgrade, and implement ERP<br>solutions to meet your needs.</p></div></div>

<div class="card" style="left:129px;top:1985px;width:455px;height:134px"><div class="ic"><span>
<svg width="32" height="32" viewBox="0 0 32 32"><circle cx="15" cy="17" r="12" fill="none" stroke="#fff" stroke-width="2.5"/><circle cx="15" cy="17" r="6" fill="none" stroke="#fff" stroke-width="2.5"/><path d="M15 17L29 3" stroke="#fff" stroke-width="2.5"/></svg></span></div>
<div class="txt"><h3>CRM Implementations</h3><p>Take your relationships to the<br>next level.</p></div></div>

<div class="card" style="left:616px;top:1985px;width:454px;height:134px"><div class="ic"><span>
<svg width="34" height="32" viewBox="0 0 34 32"><rect x="3" y="3" width="28" height="18" fill="none" stroke="#fff" stroke-width="2.5"/><path d="M8 16V12M14 16V9M20 16V11M17 21v8M11 29h12" stroke="#fff" stroke-width="2.5"/></svg></span></div>
<div class="txt"><h3>BI and Data</h3><p>Discover, connect, and trust<br>your data.</p></div></div>

<div class="card" style="left:305px;top:2156px;width:591px;height:150px"><div class="ic" style="margin-left:34px"><span style="font-size:13px">Elevra<br><small style="font-size:7px">By Norvalith</small></span></div>
<div class="txt" style="margin-left:24px"><h3>Building the Right Team of People</h3><p>Hire resources for your transformation journey.</p></div></div>

<p class="abs body" style="left:0;width:1200px;text-align:center;top:2355px">Find out how Norvalith can help you put all the pieces together and get them done.</p>

<!-- our team -->
<h2 class="abs h2" style="left:82px;top:2598px">Our Team</h2>
<p class="abs body" style="left:86px;top:2676px;width:509px">The world has changed in the past twenty years.The people you need might not all work for one company. Our clients want the best resources, available quickly. That’s why, in addition to our team of experts, we partner with:</p>
<ul class="abs checks" style="left:86px;top:2838px;width:500px">
  <li style="margin-bottom:30px"><svg width="20" height="18" viewBox="0 0 20 18"><rect x="1" y="3" width="14" height="14" fill="none" stroke="#555" stroke-width="1.6"/><path d="M4 9l4 4 10-11" fill="none" stroke="#555" stroke-width="2"/></svg>A large network of expert consultants who are the best at what they do,</li>
  <li><svg width="20" height="18" viewBox="0 0 20 18"><rect x="1" y="3" width="14" height="14" fill="none" stroke="#555" stroke-width="1.6"/><path d="M4 9l4 4 10-11" fill="none" stroke="#555" stroke-width="2"/></svg>Service providers all over the world to provide the resources and value that are right for you, available 24 x 7.</li>
</ul>
<p class="abs body" style="left:83px;top:3002px;width:520px;line-height:26px">People are invariably at the center of our customer’s success. Find out how we can add our experts to yours.</p>
<div class="ph" style="left:657px;top:2643px;width:394px;height:294px;background:linear-gradient(135deg,#d8d2c8,#7d746c 50%,#3f3c3a)" role="img" aria-label="Photo of a team meeting in an office"></div>
<div class="ph" style="left:845px;top:2830px;width:269px;height:222px;background:linear-gradient(135deg,#8a5a3a,#3a3f55 55%,#cfc9c2);border:4px solid #fff" role="img" aria-label="Photo of a consultant working on a laptop"></div>

<!-- testimonials -->
<div class="abs band-test"></div>
<h2 class="abs h2" style="left:0;width:1200px;text-align:center;top:3258px">Testimonials</h2>
<div class="quote" style="left:86px;top:3402px"><div class="name">Dario Vell</div><div class="stars">★★★★★</div><div class="mark">”</div>
<p>Lorem ipsum dolor sit amet, consectetur adipiscing elit. Sed vitae lobortis libero, at ultricies odio. Suspendisse vel sem in turpis tempus pretium. Etiam iaculis tortor sed egestas porttitor. Curabitur molestie pretium leo, quis sollicitudin nisi feugiat efficitur. Integer maximus elementum posuere tortor quis imperdiet.</p></div>
<div class="avatar" style="left:86px;top:3370px" role="img" aria-label="Portrait of client"></div>
<div class="quote" style="left:612px;top:3402px"><div class="name">Mara Quist</div><div class="stars">★★★★★</div><div class="mark">”</div>
<p>Lorem ipsum dolor sit amet, consectetur adipiscing elit. Sed vitae lobortis libero, at ultricies odio. Suspendisse vel sem in turpis tempus pretium. Etiam iaculis tortor sed egestas porttitor. Curabitur molestie pretium leo, quis sollicitudin nisi feugiat efficitur. Integer maximus elementum posuere tortor quis imperdiet.</p></div>
<div class="avatar" style="left:612px;top:3370px" role="img" aria-label="Portrait of client"></div>
<div class="arrow" style="left:25px;top:3545px">‹</div>
<div class="arrow" style="left:1138px;top:3545px">›</div>

<!-- technologies -->
<h2 class="abs h2" style="left:0;width:1200px;text-align:center;top:3968px">Technologies</h2>
<div class="arrow" style="left:95px;top:4140px;background:#999">‹</div>
<div class="tech" style="left:200px;width:180px">Corvanta</div>
<div class="tech" style="left:405px;width:160px">Quadra</div>
<div class="tech" style="left:620px;width:160px">Helix</div>
<div class="tech" style="left:820px;width:180px">Osmira</div>
<div class="arrow" style="left:1068px;top:4140px;background:#999">›</div>

<!-- footer -->
<div class="abs footer"></div>
<div class="abs f-brand">Norvalith</div>
<div class="abs socials" aria-label="Social links"><span></span><span></span><span></span><span></span></div>

<div class="abs" style="left:390px;top:4460px"><div class="f-head">QUICK LINKS</div>
<ul class="f-links" style="margin-top:22px"><li>About Us</li><li>Services</li><li>Insights</li><li>Join Us</li><li>Contact Us</li></ul></div>

<div class="abs" style="left:573px;top:4460px"><div class="f-head">CONTACT US</div>
<div class="f-contact" style="margin-top:26px">
<div class="row"><span class="box"><svg width="14" height="14" viewBox="0 0 14 14"><path d="M3 1l2 3-1.5 1.5a8 8 0 0 0 5 5L10 9l3 2-1.5 2.5C6 13 1 8 .5 2.5z" fill="#bbb"/></svg></span>+012 555 0147</div>
<div class="row" style="font-size:15px"><span class="box"><svg width="14" height="10" viewBox="0 0 14 10"><rect x=".5" y=".5" width="13" height="9" fill="none" stroke="#bbb"/><path d="M.5 .5l6.5 5 6.5-5" fill="none" stroke="#bbb"/></svg></span>info@norvalith.example</div>
<div class="row" style="font-size:15px;line-height:18px"><span class="box"><svg width="10" height="14" viewBox="0 0 10 14"><path d="M5 13S1 8 1 5a4 4 0 0 1 8 0c0 3-4 8-4 8z" fill="none" stroke="#bbb" stroke-width="1.4"/><circle cx="5" cy="5" r="1.5" fill="#bbb"/></svg></span>Address line Dummy Here<br>Address line Here</div>
</div></div>

<div class="abs" style="left:866px;top:4460px;width:250px"><div class="f-head">OUR NEWSLETTER</div>
<p style="color:#ddd;font-size:15px;line-height:20px;margin-top:22px">Subscribe our newsletter to get the latest news.</p>
<div style="background:#fff;height:34px;margin-top:22px"></div>
<div class="btn" style="width:124px;height:36px;margin-top:18px;font-size:13px">SUBSCRIBE</div></div>

<div class="abs copy">Copyright © 2023 All Rights Reserved By Norvalith</div>

</body>
</html>
```